Business Card Design Project

My business sells promotional merchandise to large blue chip companies. Gear like polo shirts, drink bottles, pens, basically anything that you can put a company logo onto.

I need the following elements included:
Logo as attached
Peter Hallorand Managing Director
21 Kestrel Court Thornlea 4168
mobile 0438 612054
email tidewell@tidewellcoastal.com.au

Promotional Merchandise with a difference

Mature age Marketing Managers

Business

```html
<!DOCTYPE html>
<html lang="en">
<head>
<meta charset="utf-8">
<title>Tidewell Business Card</title>
<link rel="stylesheet" href="https://fonts.googleapis.com/css2?family=Spectral:wght@500;600;700&display=swap">
<style>
  :root {
    --page: #ffffff;
    --ink: #1a3a7a;
    --card-base: #c6cee2;
    --card-light: #d6e2f0;
    --card-cyan: #c2e0ef;
  }
  * { margin: 0; padding: 0; box-sizing: border-box; }
  html, body {
    width: 1200px;
    height: 900px;
    overflow: hidden;
    background: var(--page);
  }
  .canvas {
    position: relative;
    width: 1200px;
    height: 900px;
  }
  .card {
    position: absolute;
    left: 0;
    top: 106px;
    width: 1200px;
    height: 684px;
    overflow: hidden;
    font-family: "Spectral", Georgia, serif;
    color: var(--ink);
  }
  .card-background {
    position: absolute;
    inset: 0;
    background:
      radial-gradient(ellipse 55% 45% at 55% 0%, var(--card-cyan) 0%, rgba(194, 224, 239, 0) 100%),
      linear-gradient(165deg, var(--card-light) 0%, var(--card-base) 60%, var(--card-base) 100%);
  }
  .contact {
    position: absolute;
    left: 54px;
    top: 0;
  }
  .contact p {
    position: absolute;
    left: 0;
    white-space: nowrap;
    font-weight: 600;
    letter-spacing: 1.5px;
  }
  .contact .name {
    top: 118px;
    font-size: 46px;
    font-weight: 700;
    letter-spacing: 2px;
  }
  .contact .role { top: 188px; font-size: 32px; }
  .contact .address { top: 252px; font-size: 34px; }
  .contact .mobile { top: 334px; font-size: 34px; }
  .contact .email { top: 400px; font-size: 32px; }
  .contact .web { top: 464px; font-size: 32px; }
  .tagline {
    position: absolute;
    left: 54px;
    top: 582px;
    font-size: 26px;
    font-weight: 600;
    letter-spacing: 1.5px;
    white-space: nowrap;
  }
  .brand-name {
    position: absolute;
    right: 52px;
    top: 545px;
    font-size: 64px;
    font-weight: 600;
    letter-spacing: 4px;
    white-space: nowrap;
  }
</style>
</head>
<body>
  <main class="canvas">
    <section class="card">
      <div class="card-background" role="img" aria-label="Soft pale blue textured background with faint flowing light bands"></div>

      <div class="contact">
        <p class="name">Peter Hallorand</p>
        <p class="role">Managing Director</p>
        <p class="address">21 Kestrel Court Thornlea 4168</p>
        <p class="mobile">M-0438 612054</p>
        <p class="email">E-tidewell@tidewellcoastal.com.au</p>
        <p class="web">www.tidewellcoastal.com.au</p>
      </div>

      <p class="tagline">Promotional Merchandise with a difference</p>
      <p class="brand-name">TIDEWELL</p>
    </section>
  </main>
</body>
</html>
```